Business Card Design Project

Hello! We need a business card design for a new company opening up in Downtown Dallas called Marbury Cupcakes. We are a cupcake factory and our primary colors are Tiffany Blue and Brown. We want to have a design that can be used for multiple positions (Owner/Operations Manager, Assistant Operations Manager, Decorator, Baker, Corporate Sale Rep, Special Events Rep etc) We would like for it to be double sided. Use the following information in your designs:

Renata Vankirk
Assistant Operations Manager
renata@marburycupcakes.example
T555.318.4907

Store Hours:
Mon-Thur 10am-9pm
Fri-Sat 10am-10pm
Sun 12pm-7pm

website: www.marburycupcakes.example

Address: 2735 Birch Ave, Dallas TX 70519

The logo is attached.

Industry/Entity Type

Business

Requirements
Must have
• It must be Tiffany Blue and Brown.
Nice to have
• Nice for it to be double sided.
Should not have
• No graphics like a cupcake. Just the word logo.

```html
<!DOCTYPE html>
<html lang="en">
<head>
<meta charset="utf-8">
<title>Marbury Cupcakes — Business Cards</title>
<link rel="stylesheet" href="https://fonts.googleapis.com/css2?family=Open+Sans:ital,wght@0,400;0,600;0,700;1,400&display=swap">
<style>
  :root {
    --backdrop: #e3e4e6;
    --paper: #eeedea;
    --brown: #4f0a05;
    --tiffany: #3fc3c6;
    --white: #ffffff;
    --swirl-tint: #bfe9ea;
  }
  * { box-sizing: border-box; margin: 0; padding: 0; }
  html, body {
    width: 1200px; height: 800px; overflow: hidden;
    background: var(--backdrop);
    font-family: "Open Sans", Arial, sans-serif;
  }
  .canvas {
    position: relative; width: 1200px; height: 800px;
    display: flex; align-items: center; justify-content: center; gap: 40px;
  }
  .card {
    position: relative; width: 540px; height: 309px;
    background: var(--paper); overflow: hidden;
    box-shadow: 0 6px 18px rgba(0,0,0,.12);
  }
  .card__band {
    position: absolute; left: 0; right: 0; bottom: 0;
    background: var(--brown);
  }
  .card--front .card__band { height: 56%; }
  .card--back .card__band { height: 50%; }

  .swirl {
    position: absolute; width: 46px; height: 46px; border-radius: 50%;
    background: radial-gradient(circle, var(--swirl-tint) 0%, rgba(191,233,234,0) 72%);
  }
  .swirl--top-left { left: 6px; top: 6px; }
  .swirl--band-edge { right: 6px; }
  .card--front .swirl--band-edge { top: 118px; }
  .card--back .swirl--band-edge { top: 132px; }

  .wordmark {
    position: absolute; color: var(--tiffany);
    font-weight: 600; font-size: 30px; letter-spacing: .5px; white-space: nowrap;
  }
  .card--front .wordmark { left: 150px; top: 48px; }
  .card--back .wordmark { right: 44px; top: 56px; font-size: 27px; }

  .holder { position: absolute; color: var(--white); }
  .card--front .holder { left: 190px; top: 166px; }
  .holder__name { font-weight: 700; font-size: 19px; }
  .holder__title { font-size: 16px; margin-top: 2px; }

  .card--back .holder { left: 26px; top: 26px; color: var(--tiffany); }
  .card--back .holder__name { font-size: 16px; }
  .card--back .holder__title { font-size: 13px; font-style: italic; margin-top: 0; }

  .contact {
    position: absolute; top: 172px; list-style: none;
    color: var(--white); font-size: 11.5px; line-height: 1.3;
  }
  .contact--left { left: 26px; }
  .contact--right { left: 296px; }
  .contact li { display: flex; align-items: flex-start; gap: 10px; margin-bottom: 11px; }
  .contact svg { flex: none; width: 16px; height: 16px; fill: none; stroke: var(--tiffany); stroke-width: 1.6; }
  .contact svg .solid { fill: var(--tiffany); stroke: none; }
</style>
</head>
<body>
<main class="canvas">

  <section class="card card--front" aria-label="Card front">
    <div class="card__band"></div>
    <div class="swirl swirl--top-left" role="img" aria-label="Tiffany blue swirl ornament"></div>
    <div class="swirl swirl--band-edge" role="img" aria-label="Tiffany blue swirl ornament"></div>
    <div class="wordmark">Marbury Cupcakes</div>
    <div class="holder">
      <p class="holder__name">Renata Vankirk</p>
      <p class="holder__title">Assistant Operations Manager</p>
    </div>
  </section>

  <section class="card card--back" aria-label="Card back">
    <div class="card__band"></div>
    <div class="swirl swirl--top-left" role="img" aria-label="Tiffany blue swirl ornament"></div>
    <div class="swirl swirl--band-edge" role="img" aria-label="Tiffany blue swirl ornament"></div>
    <div class="holder">
      <p class="holder__name">Renata Vankirk</p>
      <p class="holder__title">Assistant Operations Manager</p>
    </div>
    <div class="wordmark">Marbury Cupcakes</div>

    <ul class="contact contact--left">
      <li>
        <svg viewBox="0 0 16 16" aria-hidden="true"><rect x="1.5" y="3.5" width="13" height="9"/><path d="M1.5 3.5 8 9l6.5-5.5"/></svg>
        <span>renata@marburycupcakes.example</span>
      </li>
      <li>
        <svg viewBox="0 0 16 16" aria-hidden="true"><rect x="4.5" y="1.5" width="7" height="13" rx="1.5"/><path d="M7 12.5h2"/></svg>
        <span>555.318.4907</span>
      </li>
      <li>
        <svg viewBox="0 0 16 16" aria-hidden="true"><circle cx="8" cy="8" r="6.5"/><path d="M1.5 8h13M8 1.5c-3 3.5-3 9.5 0 13M8 1.5c3 3.5 3 9.5 0 13"/></svg>
        <span>www.marburycupcakes.example</span>
      </li>
    </ul>

    <ul class="contact contact--right">
      <li>
        <svg viewBox="0 0 16 16" aria-hidden="true"><path d="M1.5 8 8 2l6.5 6M3.5 6.5v7.5h9V6.5"/><rect class="solid" x="6.5" y="10" width="3" height="4"/></svg>
        <span>2735 Birch Ave, Dallas TX 70519</span>
      </li>
      <li>
        <svg viewBox="0 0 16 16" aria-hidden="true"><circle cx="8" cy="8" r="6.5"/><path d="M8 4v4.5l3 1.5"/></svg>
        <span>Mon-Thur 10am-9pm<br>Fri-Sat 10am-10pm<br>Sun 12pm-7pm</span>
      </li>
    </ul>
  </section>

</main>
</body>
</html>
```